Naturopath specialising in Children's Health

I have just started working in a new clinic where I will be predominantly treating children so I would like to rebrand with a business card that reflects this.

I would like a clever design which is subtly playful and will attract children and parents alike, while maintaining a professional look. It must also reflect that I utilize natural medicine - including herbal medicine and nutrition as part of my treatment. Employing the use of a plant or herb would be ideal. I had envisioned the image of a dandelion blowing in the wind (or being blown by a child) as a great combination of the playful yet natural medicine I am trying to ecompass in the card.

I would like to use yellow, orange, blue or green as the dominant colour for the card.

The front of the card should contain the logo and the words 'Maribel Stroud - Naturopath.'

The back of the card should contain the following details:
Maribel Stroud BHSc Nat, Dip RM
Naturopath, Herbalist, Nutritionist, Iridologist, Remedial Massage Therapist, Reiki Practitioner
0417 382 961
Thistle Kenwick - (02) 9463 1508
maribel.stroud@fernmail.example
HWPA 47183

```html
<!DOCTYPE html>
<html lang="en">
<head>
<meta charset="utf-8">
<title>Maribel Stroud – Naturopath business card</title>
<link rel="stylesheet" href="https://fonts.googleapis.com/css2?family=Pinyon+Script&family=Cormorant+Garamond:wght@500&family=Arimo:wght@400&display=swap">
<style>
  :root {
    --page-bg: #e9e8e4;
    --card-yellow: #f8f400;
    --card-yellow-deep: #ecE700;
    --ink-green: #2d7a1c;
    --ink-green-soft: #7fb02a;
    --motif-green-strong: rgba(120, 175, 20, 0.30);
    --motif-green-light: rgba(120, 175, 20, 0.08);
  }
  * { box-sizing: border-box; margin: 0; padding: 0; }
  html, body { width: 1200px; height: 800px; overflow: hidden; }
  body {
    background: var(--page-bg);
    display: flex;
    align-items: center;
    justify-content: center;
    gap: 40px;
  }
  .card {
    position: relative;
    width: 540px;
    height: 310px;
    background: var(--card-yellow);
    overflow: hidden;
    box-shadow: 0 2px 10px rgba(0, 0, 0, 0.12);
  }
  .motif {
    position: absolute;
    border-radius: 8px;
    background: linear-gradient(180deg, var(--motif-green-strong), var(--motif-green-light));
  }

  /* Back of card */
  .card-back .dandelion-motif {
    left: 22px;
    top: 30px;
    width: 150px;
    height: 250px;
  }
  .back-details {
    position: absolute;
    left: 196px;
    top: 56px;
    right: 20px;
  }
  .practitioner-name {
    font-family: "Cormorant Garamond", serif;
    font-weight: 500;
    font-size: 20px;
    line-height: 1.2;
    color: var(--ink-green);
  }
  .practitioner-roles {
    margin-top: 8px;
    font-family: "Arimo", sans-serif;
    font-size: 11px;
    line-height: 1.5;
    color: var(--ink-green-soft);
  }
  .contact-list {
    margin-top: 52px;
    list-style: none;
    font-family: "Arimo", sans-serif;
    font-size: 14px;
    line-height: 1.35;
    color: var(--ink-green);
  }

  /* Front of card */
  .card-front .profile-haze {
    position: absolute;
    left: 0;
    top: 0;
    width: 300px;
    height: 95px;
    background: var(--card-yellow-deep);
    border-bottom-right-radius: 60px;
  }
  .card-front .dandelion-motif {
    left: 90px;
    top: 112px;
    width: 140px;
    height: 160px;
  }
  .card-front .seeds-motif {
    left: 280px;
    top: 118px;
    width: 230px;
    height: 38px;
    background: linear-gradient(90deg, var(--motif-green-strong), var(--motif-green-light));
  }
  .brand {
    position: absolute;
    right: 36px;
    top: 176px;
    text-align: right;
    font-family: "Pinyon Script", cursive;
    color: var(--ink-green);
  }
  .brand-name { font-size: 44px; line-height: 1; }
  .brand-title { font-size: 28px; line-height: 1.1; margin-top: 4px; }
</style>
</head>
<body>
  <section class="card card-back" aria-label="Back of business card">
    <div class="motif dandelion-motif" role="img" aria-label="Soft dandelion flower on a slender stem"></div>
    <div class="back-details">
      <p class="practitioner-name">Maribel Stroud BHSc Nat, Dip RM</p>
      <p class="practitioner-roles">Naturopath, Herbalist, Nutritionist, Iridologist,<br>Remedial Massage Therapist, Reiki Practitioner</p>
      <ul class="contact-list">
        <li>0417 382 961</li>
        <li>Thistle Kenwick - (02) 9463 1508</li>
        <li>maribel.stroud@fernmail.example</li>
        <li>HWPA 47183</li>
      </ul>
    </div>
  </section>

  <section class="card card-front" aria-label="Front of business card">
    <div class="profile-haze" role="img" aria-label="Faint silhouette of a child blowing"></div>
    <div class="motif dandelion-motif" role="img" aria-label="Dandelion clock on a slender stem"></div>
    <div class="motif seeds-motif" role="img" aria-label="Dandelion seeds drifting away on the wind"></div>
    <div class="brand">
      <p class="brand-name">Maribel Stroud</p>
      <p class="brand-title">Naturopath</p>
    </div>
  </section>
</body>
</html>
```